International Travel & Visas Firm needs a Schengen Visa eBook Cover Design

We need an ebook cover design for an online based travel, immigration, visas & nationality law firm called 'OrB' (orbit and borderway). We are all about helping people overcome the obstacles to travel and ensuring that people achieve their dreams and ambitions through travel to various destinations and bettering their lives.This initial ebook cover is for our downloaded pdf ebook all about Schengen visas and travelling to any of the 26 European countries that form the Schengen Zone.We want people to be excited about buying this book even before receiving it.We would like to see amazing designs that also speak to our logo and new branding.Check out https://orbitandborderway.example/schengen-visas/ and http://orbitandborderway.pages.funnelvex.example/start-your-schengen-visa-application

Target Market(s)

Travellers that want to get a visa to travel around Europe

Industry/Entity Type

Travel Industry

Colors
fbee3d
faa54b

Requirements
Must have
• - Title:
• Passport Path Primer
Nice to have
• - tagline:
• Unshackle your feet and roam 26 European Countries
• - OrB Logo
• - Reference to it being an insider's guide to Schengen Visas
• - a play on the word OrB (I am)

```html
<!DOCTYPE html>
<html lang="en">
<head>
<meta charset="utf-8">
<title>Passport Path Primer — OrB</title>
<link rel="stylesheet" href="https://fonts.googleapis.com/css2?family=Kaushan+Script&family=Montserrat:wght@300;600&display=swap">
<style>
  :root {
    --ink-dark: #1c1a18;
    --map-tan: #a8773f;
    --map-deep: #6e4a24;
    --title-yellow: #dcd843;
    --tag-white: #f4f1ea;
  }
  html, body {
    margin: 0;
    padding: 0;
    width: 750px;
    height: 1200px;
    overflow: hidden;
    background: var(--ink-dark);
  }
  .cover {
    position: relative;
    width: 750px;
    height: 1200px;
    overflow: hidden;
    font-family: "Montserrat", sans-serif;
  }
  .cover-scene {
    position: absolute;
    inset: 0;
    background:
      radial-gradient(ellipse 60% 35% at 80% 40%, rgba(90,90,90,0.55), transparent 70%),
      linear-gradient(180deg, #1f1d1b 0%, #2d2722 26%, #5b3f22 42%, var(--map-tan) 62%, #9a6a36 82%, var(--map-deep) 100%);
  }
  .tagline {
    position: absolute;
    left: 0;
    right: 0;
    text-align: center;
    color: var(--tag-white);
    margin: 0;
  }
  .tagline-lead {
    top: 102px;
    font-weight: 300;
    font-size: 18px;
    letter-spacing: 4.4px;
  }
  .tagline-rule {
    position: absolute;
    top: 143px;
    left: 148px;
    width: 460px;
    height: 1.5px;
    background: var(--tag-white);
  }
  .tagline-count {
    top: 160px;
    font-weight: 600;
    font-size: 22px;
    letter-spacing: 5px;
  }
  .title {
    position: absolute;
    top: 372px;
    left: 0;
    right: 0;
    margin: 0;
    text-align: center;
    font-family: "Kaushan Script", cursive;
    font-weight: 400;
    color: var(--title-yellow);
    line-height: 150px;
    font-size: 120px;
    text-shadow: 0 2px 6px rgba(0,0,0,0.25);
  }
  .title span { display: block; }
  .publisher {
    position: absolute;
    top: 1076px;
    left: 0;
    right: 0;
    margin: 0;
    text-align: center;
    font-weight: 600;
    font-size: 20px;
    letter-spacing: 3px;
    color: var(--tag-white);
  }
</style>
</head>
<body>
  <main class="cover">
    <div class="cover-scene" role="img" aria-label="Still life of a vintage film camera and leather suitcase on an old world map, with sepia instant photos of a city street, a postcard and the Eiffel Tower"></div>

    <p class="tagline tagline-lead">UNSHACKLE YOUR FEET AND ROAM</p>
    <div class="tagline-rule"></div>
    <p class="tagline tagline-count">• 26 EUROPEAN COUNTRIES •</p>

    <h1 class="title">
      <span>Passport</span>
      <span>Path</span>
      <span>Primer</span>
    </h1>

    <p class="publisher">OrB | orbit and borderway</p>
  </main>
</body>
</html>
```